Website Redesign for a Restaurant with International Cuisine

We need a new website design for a Czech restaurant website that should be modern, simple, flexible, and mobile-friendly. We only need the PSD's, not the website coded.

-- Available images
https://files.veltrobox.com/share/9QxTmr4LpZ7wKd2NaY3bHc8Ve5

-- Our current website
https://beta.ohnivakorna.cz

-- Website we like
https://www.elpatiomorado.cz/en/
https://www.bellhavenhall.com/

## Design following pages of our current website with given effort distribution:
-- 40% Home page, https://www.ohnivakorna.cz/
-- 30% Regular Menu, https://www.ohnivakorna.cz/stala_nabidka
-- 20% Contacts, https://www.ohnivakorna.cz/kontakty
-- 10% About Us, https://www.ohnivakorna.cz/o_nas

## Our strengths
-- Cozy, clean environment
-- we use USDA Prime and USDA Choice class meat
-- helpful, friendly staff
-- high quality traditional international cuisine (that is rare)
-- unique wood-fired oven
-- open parking space

## Our weaknesses
-- longer wait times (especially on weekends)
-- slightly expensive prices

Target Market(s)

People interested in gastronomy looking for high quality dishes.

Industry/Entity Type

Restaurant

Number of Pages Required

4 page

Font styles to use
Serif
Sans Serif

Colors

Designer to choose colors to be used in the design.

Requirements
Must have
• -- Preserve current content structure and the order of indiviual elements (use https://www.ohnivakorna.cz).
• -- Emphasize both weekend events and daily deals. Weekend events are more of a priority.
• -- Also emphasize logo and the restaurant owner’s profile and the link to Google Maps.
• -- Mobile-friendly
• -- Use photos from our gallery to maximize authenticity:
• https://files.veltrobox.com/share/9QxTmr4LpZ7wKd2NaY3bHc8Ve5
Nice to have
• -- Solutions with higher accessibility compliance (WCAG) are preferred.
• -- You may add important links/buttons or rephrase them if necessary.
Should not have
• -- Do not use photos from the current website. You may use externally sourced images if necessary.
• -- Do not use endless animations (carousels).
• -- Do not use embedded content (e.g. interactive map). You may or may not use a map as background decoration for that section.
• -- Nothing too crowded / busy.
• -- Not too many colors.

```html
<!DOCTYPE html>
<html lang="en">
<head>
<meta charset="utf-8">
<title>Ember Vale – Home</title>
<link rel="stylesheet" href="https://fonts.googleapis.com/css2?family=Montserrat:wght@400;500;700;800;900&display=swap">
<style>
  :root {
    --brand-red: #c0221f;
    --white: #ffffff;
    --page-bg: #f4f4f4;
    --photo-dark: #1d1d20;
    --photo-mid: #4a2a24;
    --photo-meat: #7a3a30;
  }
  * { box-sizing: border-box; margin: 0; padding: 0; }
  html, body { width: 1200px; height: 1200px; overflow: hidden; background: var(--page-bg); }
  body { font-family: "Montserrat", sans-serif; color: var(--white); }

  .site {
    position: absolute; left: 0; top: 225px;
    width: 1200px; height: 750px; overflow: hidden;
    border-top: 4px solid var(--brand-red);
  }
  .hero-photo {
    position: absolute; inset: 0;
    background:
      radial-gradient(ellipse 30% 25% at 12% 18%, #6b6a2c 0%, transparent 70%),
      radial-gradient(ellipse 45% 35% at 75% 65%, var(--photo-meat) 0%, transparent 75%),
      radial-gradient(ellipse 30% 25% at 40% 80%, #8a4a42 0%, transparent 75%),
      radial-gradient(ellipse 20% 20% at 50% 12%, #9a9aa0 0%, transparent 80%),
      linear-gradient(160deg, #2b2b30 0%, var(--photo-dark) 45%, var(--photo-mid) 100%);
  }

  .main-nav a {
    position: absolute; top: 59px;
    font-weight: 700; font-size: 19px; letter-spacing: -0.5px;
    color: var(--white); text-decoration: none; text-transform: uppercase;
  }
  .nav-about { left: 116px; }
  .nav-menu { left: 264px; }
  .nav-gallery { left: 370px; }
  .nav-news { left: 760px; }
  .nav-contact { left: 966px; }
  .lang-switch { position: absolute; left: 1141px; top: 53px; width: 37px; height: 37px; }

  .brand {
    position: absolute; left: 0; width: 1172px; top: 28px;
    display: flex; flex-direction: column; align-items: center; gap: 10px;
  }
  .brand-mark { width: 80px; height: 80px; border-radius: 50%; background: var(--brand-red); }
  .brand-name { font-weight: 900; font-size: 38px; color: var(--brand-red); letter-spacing: -0.5px; text-transform: uppercase; }

  .hero-frame { position: absolute; left: 118px; top: 292px; width: 944px; height: 147px; }
  .hero-title {
    position: absolute; left: 0; width: 1176px; top: 254px; text-align: center;
    font-weight: 800; font-size: 62px; letter-spacing: -2px; text-transform: uppercase;
    white-space: nowrap;
  }
  .hero-lead {
    position: absolute; left: 186px; width: 800px; top: 345px; text-align: center;
    font-weight: 500; font-size: 18.5px; line-height: 29px;
  }
  .cta {
    position: absolute; left: 451px; top: 517px; width: 258px; height: 66px;
    border-radius: 33px; background: var(--white); color: var(--brand-red);
    display: flex; align-items: center; justify-content: center; gap: 14px;
    font-weight: 800; font-size: 19px; letter-spacing: -0.5px; text-decoration: none;
  }

  .feature-band { position: absolute; left: 0; bottom: 0; width: 1200px; height: 54px; background: var(--brand-red); }
  .feature-badge {
    position: absolute; top: 652px; width: 106px; height: 106px; border-radius: 50%;
    background: var(--brand-red); display: flex; align-items: center; justify-content: center;
    padding-bottom: 10px;
  }
  .badge-meat { left: 184px; }
  .badge-years { left: 530px; }
  .badge-fresh { left: 886px; }
  .badge-years span { font-weight: 500; font-size: 44px; letter-spacing: -2px; }
</style>
</head>
<body>
  <main class="site">
    <div class="hero-photo" role="img" aria-label="Grilled sliced steak with herb chimichurri, pepper corns and a knife on a dark wooden board"></div>

    <nav class="main-nav">
      <a class="nav-about" href="#about">About us</a>
      <a class="nav-menu" href="#menu">Menu</a>
      <a class="nav-gallery" href="#gallery">Gallery</a>
      <a class="nav-news" href="#news">News &amp; Events</a>
      <a class="nav-contact" href="#contact">Contact</a>
    </nav>
    <svg class="lang-switch" viewBox="0 0 40 40" aria-label="Čeština">
      <defs><clipPath id="flag-clip"><circle cx="20" cy="20" r="20"/></clipPath></defs>
      <g clip-path="url(#flag-clip)">
        <rect width="40" height="20" fill="#ffffff"/>
        <rect y="20" width="40" height="20" fill="#d7141a"/>
        <polygon points="0,0 20,20 0,40" fill="#11457e"/>
      </g>
    </svg>

    <div class="brand">
      <div class="brand-mark"></div>
      <div class="brand-name">Ember Vale</div>
    </div>

    <svg class="hero-frame" viewBox="0 0 944 147" fill="none" stroke="#c0221f" stroke-width="3">
      <path d="M40 2 H14 Q2 2 2 14 V133 Q2 145 14 145 H930 Q942 145 942 133 V14 Q942 2 930 2 H902"/>
    </svg>
    <h1 class="hero-title">Taste best food ever</h1>
    <p class="hero-lead">We can give you more than you think. Loremipsum dolor sit amet consectetur adip piscing dolor amet</p>

    <a class="cta" href="#info">GET MORE INFO
      <svg width="22" height="18" viewBox="0 0 22 18" fill="none" stroke="#c0221f" stroke-width="2.6" stroke-linecap="round" stroke-linejoin="round"><path d="M2 9 H19 M12 2 L19 9 L12 16"/></svg>
    </a>

    <div class="feature-band"></div>
    <div class="feature-badge badge-meat">
      <svg width="66" height="56" viewBox="0 0 66 56" fill="none" stroke="#fff" stroke-width="3" stroke-linejoin="round">
        <path d="M8 20 Q10 4 30 4 Q56 4 60 24 Q63 44 44 50 Q30 54 20 48 Q14 44 10 46 Q4 48 4 40 Q4 32 8 20 Z"/>
        <circle cx="36" cy="26" r="12"/><path d="M30 22 L40 30 M40 20 L34 32"/>
      </svg>
    </div>
    <div class="feature-badge badge-years"><span>30</span></div>
    <div class="feature-badge badge-fresh">
      <svg width="56" height="50" viewBox="0 0 56 50" fill="none" stroke="#fff" stroke-width="3" stroke-linecap="round" stroke-linejoin="round">
        <path d="M6 46 Q20 30 52 30 Q44 46 24 44 Q14 43 6 46 Z"/>
        <path d="M16 40 Q10 26 16 6 Q30 18 26 36"/>
        <path d="M6 46 L40 34"/>
      </svg>
    </div>
  </main>
</body>
</html>
```